Falcrest security business card

Looking for a business card for my security company

Target Market(s)

Security

Industry/Entity Type

Security

Contact Information for Business Card

Name - Gil Marston. Title - General manager - direct 314 862.4490 website www. falcrestsecurityservices.example email - gil@ falcrestsecurityservices.example

Requirements
Must have
• Logo attached

```html
<!DOCTYPE html>
<html lang="en">
<head>
<meta charset="utf-8">
<title>Falcrest Security – Business Card</title>
<link rel="stylesheet" href="https://fonts.googleapis.com/css2?family=Marcellus&family=Josefin+Sans:ital,wght@1,300&display=swap">
<style>
  :root {
    --backdrop: #e6be7a;
    --card-navy: #0b0f1f;
    --gold: #c9a24e;
    --gold-light: #d9b567;
    --ghost: #151b2b;
  }
  * { margin: 0; padding: 0; box-sizing: border-box; }
  html, body { width: 972px; height: 1200px; overflow: hidden; }
  body { background: var(--backdrop); position: relative; }

  .card {
    position: absolute;
    left: 102px;
    width: 766px;
    height: 466px;
    background: var(--card-navy);
    overflow: hidden;
  }
  .card--front { top: 88px; }
  .card--back { top: 640px; }

  .brand-name {
    position: absolute;
    font-family: "Marcellus", serif;
    color: var(--gold);
    letter-spacing: 1px;
    white-space: nowrap;
  }
  .card--front .brand-name--corner {
    right: 34px;
    top: 38px;
    font-size: 24px;
  }
  .brand-name--ghost {
    left: 380px;
    top: 372px;
    font-size: 68px;
    color: var(--ghost);
    letter-spacing: 2px;
  }

  .holder-name {
    position: absolute;
    left: 51px;
    top: 205px;
    font-family: "Marcellus", serif;
    font-size: 43px;
    color: var(--gold);
    letter-spacing: 0.5px;
    white-space: nowrap;
  }
  .holder-title {
    position: absolute;
    left: 51px;
    top: 255px;
    font-family: "Josefin Sans", sans-serif;
    font-style: italic;
    font-weight: 300;
    font-size: 19px;
    color: var(--gold);
    letter-spacing: 1.5px;
  }

  .accent-bar {
    position: absolute;
    left: 51px;
    top: 287px;
    width: 25px;
    height: 179px;
    background: var(--gold);
  }

  .contact-list { list-style: none; }
  .contact-item {
    position: absolute;
    left: 52px;
    display: flex;
    align-items: center;
    gap: 9px;
    font-family: "Marcellus", serif;
    font-size: 13px;
    color: var(--gold-light);
    white-space: nowrap;
  }
  .contact-item--phone { top: 320px; }
  .contact-item--email { top: 355px; }
  .contact-item--web { top: 389px; }
  .contact-icon { width: 22px; height: 22px; flex: none; }

  .back-field {
    position: absolute;
    inset: 0;
    background: var(--card-navy);
  }
  .card--back .brand-name--center {
    left: 0;
    right: 0;
    top: 200px;
    text-align: center;
    font-size: 54px;
    letter-spacing: 3px;
  }
</style>
</head>
<body>

  <section class="card card--front" aria-label="Business card front">
    <div class="brand-name brand-name--corner">FALCREST</div>
    <div class="brand-name brand-name--ghost" aria-hidden="true">FALCREST</div>

    <h1 class="holder-name">GIL MARSTON</h1>
    <p class="holder-title">GENERAL MANAGER</p>

    <div class="accent-bar"></div>

    <ul class="contact-list">
      <li class="contact-item contact-item--phone">
        <svg class="contact-icon" viewBox="0 0 22 22" aria-hidden="true">
          <circle cx="11" cy="11" r="10" fill="var(--card-navy)" stroke="#1a1d2a" stroke-width="1.2"/>
          <path d="M7.5 6.5 l2 -0.5 l1 2.6 l-1.2 1 a6 6 0 0 0 3 3 l1 -1.2 l2.6 1 l-0.5 2 a1.5 1.5 0 0 1 -1.6 1 a9 9 0 0 1 -7.3 -7.3 a1.5 1.5 0 0 1 1 -1.6z" fill="none" stroke="#1a1d2a" stroke-width="1.2" stroke-linejoin="round"/>
        </svg>
        <span>314 862.4490</span>
      </li>
      <li class="contact-item contact-item--email">
        <svg class="contact-icon" viewBox="0 0 22 22" aria-hidden="true">
          <circle cx="11" cy="11" r="10" fill="var(--card-navy)" stroke="#1a1d2a" stroke-width="1.2"/>
          <rect x="6" y="7.5" width="10" height="7" rx="1" fill="none" stroke="#1a1d2a" stroke-width="1.3"/>
          <path d="M6 8 l5 4 l5 -4" fill="none" stroke="#1a1d2a" stroke-width="1.3"/>
        </svg>
        <span>gil@falcrestsecurityservices.example</span>
      </li>
      <li class="contact-item contact-item--web">
        <svg class="contact-icon" viewBox="0 0 22 22" aria-hidden="true">
          <circle cx="11" cy="11" r="10" fill="var(--card-navy)" stroke="#1a1d2a" stroke-width="1.2"/>
          <text x="11" y="13.5" text-anchor="middle" font-family="sans-serif" font-size="6" fill="#1a1d2a">www</text>
        </svg>
        <span>www.falcrestsecurityservices.example</span>
      </li>
    </ul>
  </section>

  <section class="card card--back" aria-label="Business card back">
    <div class="back-field" role="img" aria-label="Repeating pattern of faint leaping big cat silhouettes on navy"></div>
    <div class="brand-name brand-name--center">FALCREST</div>
  </section>

</body>
</html>
```